need corporate, modern business card created for Consulting Company

I need a slick business card using elements from my website, as well as, integrating my pixelharbor-created logo (see files).

The business card needs to be:
1. Corporate and modern
2. Clean and professional

I've included a PSD with the logo/icon that you can use to create it. Feel free to try a metallic finish on the logo, make it bigger/small, underlay it. Whatever you need to do to make my card stand out.

Try a black background, or white background or gray.

The idea is for my card to be memorable as well as professional and corporate.

Target Market(s)

Corporate business in the US and Canada.

Industry/Entity Type

Business

Contact Information for Business Card

Business Leveraging Technology
Malcolm Tudd, Senior Partner
office: 1 877 555 0143
mobile: 1 519 555 0172
website: http://www.vextorial.com

Requirements
Must have
• Card-related information
• corporate, yet modern
• clean and professional
• incorporate the icon only
• must have an editable form when complete!
Nice to have
• metallic icon might be cool
• try it with white or black

```html
<!DOCTYPE html>
<html lang="en">
<head>
<meta charset="utf-8">
<title>Vextorial Business Card</title>
<link rel="stylesheet" href="https://fonts.googleapis.com/css2?family=Open+Sans:wght@400;600&family=PT+Sans:wght@400&display=swap">
<style>
  :root {
    --bg-deep: #0e2f3d;
    --bg-mid: #14506a;
    --bg-glow: #1184a6;
    --card: #1f1f1f;
    --brand-blue: #3a6db5;
    --white: #ffffff;
    --muted: #7a7a7a;
    --rule: #5a5a5a;
  }
  * { margin: 0; padding: 0; box-sizing: border-box; }
  html, body { width: 1200px; height: 800px; overflow: hidden; }
  body {
    position: relative;
    font-family: "Open Sans", Arial, sans-serif;
    background:
      radial-gradient(ellipse 520px 260px at 760px 60px, var(--bg-glow), transparent 75%),
      linear-gradient(180deg, var(--bg-mid) 0%, var(--bg-deep) 100%);
  }
  .card {
    position: absolute;
    background: var(--card);
    box-shadow: 4px 6px 10px rgba(0,0,0,0.45);
  }
  .card-front { left: 72px; top: 27px; width: 580px; height: 330px; }
  .card-back  { left: 585px; top: 421px; width: 581px; height: 332px; overflow: hidden; }

  .wordmark {
    position: absolute;
    display: flex;
    align-items: center;
    gap: 14px;
    font-family: "Open Sans", Arial, sans-serif;
    font-weight: 600;
    color: var(--brand-blue);
    line-height: 1;
  }
  .wordmark-mark { background: var(--brand-blue); flex: none; }
  .card-front .wordmark { left: 132px; top: 154px; font-size: 52px; }
  .card-front .wordmark-mark { width: 30px; height: 30px; }

  .name-band { position: absolute; left: 0; top: 32px; }
  .holder-name {
    position: absolute; left: 40px; top: 42px;
    font-family: "PT Sans", Arial, sans-serif;
    font-size: 26px; color: var(--white);
  }
  .holder-tagline {
    position: absolute; left: 40px; top: 76px;
    font-size: 8.5px; color: var(--white);
  }
  .card-back .wordmark-head { left: 290px; top: 58px; font-size: 46px; }
  .card-back .wordmark-head .wordmark-mark { width: 26px; height: 26px; }

  .divider {
    position: absolute; left: 277px; top: 175px;
    width: 1px; height: 119px; background: var(--rule);
  }
  .contact {
    position: absolute;
    display: flex; align-items: center;
    color: var(--white); font-size: 14px;
  }
  .contact svg { flex: none; margin-right: 6px; }
  .contact-label { font-size: 6.5px; color: var(--brand-blue); margin-right: 8px; margin-top: 6px; }
  .contact-office { left: 38px; top: 202px; }
  .contact-mobile { left: 350px; top: 202px; }
  .contact-web    { left: 348px; top: 247px; }

  .card-back .wordmark-foot {
    left: 12px; top: 305px; font-size: 14px; gap: 5px; color: var(--muted);
  }
  .wordmark-foot .wordmark-mark { width: 8px; height: 8px; background: var(--muted); }
</style>
</head>
<body>

  <section class="card card-front" aria-label="Card front">
    <div class="wordmark">
      <span class="wordmark-mark"></span>
      <span class="wordmark-name">vextorial</span>
    </div>
  </section>

  <section class="card card-back" aria-label="Card back">
    <svg class="name-band" width="300" height="76" viewBox="0 0 300 76" aria-hidden="true">
      <path d="M0 0 H278 A48 48 0 0 0 278 76 H0 Z" fill="var(--brand-blue)"/>
    </svg>
    <p class="holder-name">Malcolm Tudd</p>
    <p class="holder-tagline">Business Leveraging Technology</p>

    <div class="wordmark wordmark-head">
      <span class="wordmark-mark"></span>
      <span class="wordmark-name">vextorial</span>
    </div>

    <div class="divider"></div>

    <div class="contact contact-office">
      <svg width="26" height="26" viewBox="0 0 26 26" aria-hidden="true">
        <path d="M13 1 L25 12 H22 V26 H4 V12 H1 Z" fill="var(--brand-blue)"/>
      </svg>
      <span class="contact-label">office :</span>
      <span class="contact-value">1 877 555 0143</span>
    </div>

    <div class="contact contact-mobile">
      <svg width="18" height="28" viewBox="0 0 18 28" aria-hidden="true">
        <rect x="1" y="1" width="16" height="26" rx="2" fill="none" stroke="var(--brand-blue)" stroke-width="2"/>
        <rect x="3.5" y="4" width="11" height="16" fill="var(--brand-blue)"/>
        <circle cx="9" cy="23.5" r="1.5" fill="var(--brand-blue)"/>
      </svg>
      <span class="contact-label">Mobile :</span>
      <span class="contact-value">1 519 555 0172</span>
    </div>

    <div class="contact contact-web">
      <svg width="26" height="26" viewBox="0 0 26 26" aria-hidden="true" fill="none" stroke="var(--brand-blue)" stroke-width="1.6">
        <circle cx="13" cy="13" r="11.5"/>
        <ellipse cx="13" cy="13" rx="5" ry="11.5"/>
        <line x1="1.5" y1="13" x2="24.5" y2="13"/>
        <line x1="13" y1="1.5" x2="13" y2="24.5"/>
        <path d="M3.5 7 H22.5 M3.5 19 H22.5"/>
      </svg>
      <span class="contact-label">Web :</span>
      <span class="contact-value">www.vextorial.com</span>
    </div>

    <div class="wordmark wordmark-foot">
      <span class="wordmark-mark"></span>
      <span class="wordmark-name">vextorial</span>
    </div>
  </section>

</body>
</html>
```